Business Card Design Project

This is the first time we use our new logo. We need a business card that we can use both on our institutional corporate relationships and also that works for our staff that deals with consumers directly.

VELUNDA is a new company dedicated to empower consumers and to provide them with the best choices for specialized health care using the latest telemedicine technology (medicine at a distance via videoconference).

We want to print this cards in high quality materials and process. We will like designs that allow us to use UV spot varnish and other techniques that will differentiate us.

We are including Two different versions of Color logos. In addition we are including white over black background logos. Those can be used replacing the black for a color.

Please note this is the first time we will be creating any corporate materials with our new logo and colors.

Target Market(s)

34+ consumers of medium high and high socioeconomic levels.

Industry/Entity Type

Health

Requirements
Must have
• Our logo on its original colors
Should not have
• Any other graphical element or design that is not our logo

```html
<!DOCTYPE html>
<html lang="en">
<head>
<meta charset="utf-8">
<title>VELUNDA Business Card</title>
<link rel="stylesheet" href="https://fonts.googleapis.com/css2?family=Jost:wght@400;500;600&display=swap">
<style>
  :root {
    --backdrop: #9b9b9b;
    --navy: #1b4674;
    --navy-deep: #0d3a66;
    --navy-mid: #16578a;
    --blue: #2f82c4;
    --teal: #27a08a;
    --paper: #f4f4f4;
    --paper-shade: #e4e4e4;
    --white: #ffffff;
  }
  * { margin: 0; padding: 0; box-sizing: border-box; }
  html, body { width: 1200px; height: 720px; overflow: hidden; }
  body {
    background: var(--backdrop);
    font-family: "Jost", "Futura", sans-serif;
    position: relative;
  }
  .card {
    position: absolute;
    top: 205px;
    width: 540px;
    height: 310px;
    overflow: hidden;
    box-shadow: 0 4px 14px rgba(0,0,0,0.25);
  }
  /* Front */
  .card-front {
    left: 40px;
    background: linear-gradient(120deg, var(--white) 0%, var(--paper) 55%, var(--paper-shade) 100%);
    border-bottom: 4px solid var(--navy-deep);
  }
  .brand {
    position: absolute;
    left: 30px;
    top: 92px;
    display: flex;
    flex-direction: column;
    align-items: center;
  }
  .brand-dot {
    width: 34px;
    height: 34px;
    border-radius: 50%;
    background: var(--blue);
    margin-bottom: 12px;
  }
  .brand-name {
    font-size: 40px;
    font-weight: 600;
    letter-spacing: 2px;
    color: var(--navy);
    line-height: 1;
  }
  .person {
    position: absolute;
    right: 32px;
    top: 82px;
    text-align: right;
  }
  .person-name {
    font-size: 24px;
    letter-spacing: 1.5px;
    color: var(--navy);
    line-height: 1.1;
  }
  .person-name .first { font-weight: 500; }
  .person-name .last { font-weight: 400; }
  .person-role {
    font-size: 14px;
    color: var(--teal);
    margin-top: 2px;
  }
  .address {
    position: absolute;
    left: 262px;
    right: 22px;
    top: 150px;
    padding: 5px 0 6px;
    border-top: 1px solid var(--teal);
    border-bottom: 1px solid var(--teal);
    font-size: 11px;
    color: var(--navy);
    letter-spacing: 0.3px;
  }
  .contacts {
    position: absolute;
    left: 262px;
    top: 186px;
    list-style: none;
  }
  .contact {
    display: flex;
    align-items: center;
    gap: 10px;
    font-size: 13.5px;
    color: var(--navy);
    height: 21px;
    letter-spacing: 0.3px;
  }
  .contact svg { width: 13px; height: 13px; flex: none; }
  .contacts-rule {
    position: absolute;
    left: 262px;
    right: 22px;
    top: 282px;
    border-top: 1px solid var(--teal);
  }
  /* Back */
  .card-back {
    left: 620px;
    background: linear-gradient(100deg, var(--navy-mid) 0%, var(--navy-deep) 60%, #0b335c 100%);
  }
  .web-address {
    position: absolute;
    left: 0;
    right: 0;
    top: 130px;
    text-align: center;
    font-size: 14px;
    letter-spacing: 2px;
    color: var(--white);
  }
  .web-address .domain { color: var(--teal); }
  .back-brand {
    position: absolute;
    right: 26px;
    bottom: 22px;
    display: flex;
    flex-direction: column;
    align-items: center;
  }
  .back-brand .brand-dot {
    width: 18px;
    height: 18px;
    margin-bottom: 6px;
  }
  .back-brand .brand-name {
    font-size: 20px;
    color: var(--white);
    letter-spacing: 1.5px;
  }
</style>
</head>
<body>
  <section class="card card-front">
    <div class="brand">
      <span class="brand-dot"></span>
      <span class="brand-name">VELUNDA</span>
    </div>

    <div class="person">
      <p class="person-name"><span class="first">MARCUS</span> <span class="last">HALE</span></p>
      <p class="person-role">Director</p>
    </div>

    <p class="address">418 West Harbor Lane, Dunmore, PA 18512</p>

    <ul class="contacts">
      <li class="contact">
        <svg viewBox="0 0 14 14" aria-hidden="true"><rect x="3.5" y="0.5" width="7" height="13" rx="1.2" fill="none" stroke="var(--teal)" stroke-width="1.3"/><rect x="5" y="2.5" width="4" height="4" fill="var(--teal)"/></svg>
        012 5550 1947
      </li>
      <li class="contact">
        <svg viewBox="0 0 14 14" aria-hidden="true"><path d="M1 5 Q7 0 13 5 L11 6.5 L9.5 5 L4.5 5 L3 6.5 Z" fill="var(--teal)"/><rect x="2.5" y="7.5" width="9" height="5.5" rx="1" fill="var(--teal)"/></svg>
        (484) 555-0172
      </li>
      <li class="contact">
        <svg viewBox="0 0 14 14" aria-hidden="true"><rect x="0.8" y="2.5" width="12.4" height="9" fill="none" stroke="var(--teal)" stroke-width="1.3"/><path d="M1 3 L7 8 L13 3" fill="none" stroke="var(--teal)" stroke-width="1.3"/></svg>
        info@velunda.com
      </li>
      <li class="contact">
        <svg viewBox="0 0 14 14" aria-hidden="true"><circle cx="7" cy="7" r="6" fill="none" stroke="var(--teal)" stroke-width="1.3"/><ellipse cx="7" cy="7" rx="2.6" ry="6" fill="none" stroke="var(--teal)" stroke-width="1"/><line x1="1" y1="7" x2="13" y2="7" stroke="var(--teal)" stroke-width="1"/></svg>
        www.velunda.com
      </li>
    </ul>
    <div class="contacts-rule"></div>
  </section>

  <section class="card card-back">
    <p class="web-address">www.<span class="domain">velunda</span>.com</p>
    <div class="back-brand">
      <span class="brand-dot"></span>
      <span class="brand-name">VELUNDA</span>
    </div>
  </section>
</body>
</html>
```